Health & Wellness Website

Corvanta focuses on helping people with chronic health conditions through communication, education and behavior management. See the attached summary for more info on the company.

The attached wire frames should be turned into a very intuitive and simple website design. The design should have a minimal, modern, and yet still personal feel since the main point of the site is for people with chronic health conditions to be able to express themselves and find others that are like them.

There are 18 pages in the wire frames, but most of them have very similar content and page layouts. The design of the pages should to be as similar to each other as possible with most of the features and formats being repeated. The layout is not set in stone and the primary focus should be on intuitive use.

There should be two versions of the designs: one for tablets in the portrait mode (768 px) and one in the landscape mode (1024 px). These layouts should be included in the winning design.

If you would like to submit one page, I will check the posting and give feedback frequently so you don't waste your time and have to change everything.

Target Market(s)

The target market for this website has two different groups within the overall chronic health patient umbrella. The primary group are people who are under 55 yrs old and already use one or more social media sites. The other group consists of people that are older and less familiar with modern websites. The site needs to be catered to the latter and be incredibly intuitive.

Industry/Entity Type

Education

Requirements
Must have
• INTUITIVE DESIGN that is simple, minimal, and modern with a limited color palette. Tablet landscape and portrait versions are needed. Adobe Fireworks is the preferred program and will give submitted designs a huge leg up in the decision. Adobe Photoshop is the only other acceptable program to use. The designer will also need to make the social media icons, buttons, and other graphic design items that are needed for to go along with the theme. These should be vector graphics and be created either in Adobe Fireworks or Illustrator. All working files for the pages, icons, and graphics will be required once the winner is chosen.
• The necessary pages include: the landing page (long scrolling page with about and community sections); a general modal pop-up layout that includes forms and text; the template for inside of the members area (Home Page in wire frames); the community page; and the profile page (with tabs). Please include all the pages you feel it takes to communicate your design.
Nice to have
• Descriptions of transition effects and notes for the programmers are a good thing. The designer might consider adding navigation on the public landing page that scrolls with the header (This is not in the wire frames).
Should not have
• Flashy or complex features that require a lot of code to accomplish. Should not look like Pagelink.

```html
<!DOCTYPE html>
<html lang="en">
<head>
<meta charset="utf-8">
<title>Corvanta – Wellness Community</title>
<link href="https://fonts.googleapis.com/css2?family=Roboto+Condensed:wght@400;700&family=Roboto:wght@400&display=swap" rel="stylesheet">
<style>
:root{
  --ink:#4f5170;
  --ink-dark:#3f4160;
  --paper:#efeced;
  --strip:#7f7f93;
  --white:#ffffff;
  --muted:#7a7a86;
  --logo:#6f7086;
  --sky-top:#9fd0ef;
  --sky-bottom:#e6f3fa;
}
*{margin:0;padding:0;box-sizing:border-box}
html,body{width:1200px;height:1200px;overflow:hidden}
body{background:var(--paper);font-family:"Roboto",Arial,sans-serif;position:relative}
.top-strip{position:absolute;left:0;top:0;width:1200px;height:12px;background:var(--strip)}
.site-header{position:absolute;left:0;top:12px;width:1200px;height:146px;background:var(--paper)}
.brand{position:absolute;left:138px;top:104px;font-family:"Roboto Condensed",Arial,sans-serif;font-size:27px;letter-spacing:9px;color:var(--logo);font-weight:400}
.btn{position:absolute;background:var(--ink);color:var(--white);font-family:"Roboto Condensed",Arial,sans-serif;font-size:14px;display:flex;align-items:center;justify-content:center;border:1px solid var(--ink-dark);border-radius:2px}
.btn-signup{left:561px;top:44px;width:80px;height:30px}
.btn-login{left:999px;top:44px;width:80px;height:30px}
.field{position:absolute;top:44px;width:162px;height:31px;background:var(--white);border:1px solid #d8d4d6;border-radius:2px;box-shadow:inset 0 1px 2px rgba(0,0,0,.08)}
.field-user{left:656px}
.field-pass{left:828px}
.remember{position:absolute;left:656px;top:86px;font-size:12px;color:#9a9aa2;display:flex;align-items:center;gap:6px}
.remember .box{width:14px;height:14px;border:1px solid #c9c6c8;background:var(--white);border-radius:2px}
.forgot{position:absolute;left:827px;top:88px;font-size:12px;color:#9a9aa2}
.hero{position:absolute;left:0;top:158px;width:1200px;height:614px;background:var(--ink)}
.slide-frame{position:absolute;left:120px;top:39px;width:960px;height:400px;background:var(--white);box-shadow:0 18px 22px -12px rgba(0,0,0,.45)}
.slide-photo{position:absolute;left:10px;top:10px;width:940px;height:378px;background:linear-gradient(180deg,var(--sky-top),var(--sky-bottom))}
.slide-photo .slide-people{position:absolute;right:0;top:0;width:440px;height:378px;background:linear-gradient(160deg,rgba(230,190,160,.55),rgba(90,180,220,.6) 60%,rgba(80,150,60,.45))}
.slide-brand{position:absolute;left:80px;top:210px;font-family:"Roboto Condensed",Arial,sans-serif;font-size:27px;letter-spacing:10px;color:#111;font-weight:700}
.arrow{position:absolute;top:193px}
.arrow-prev{left:79px}
.arrow-next{left:1080px}
.dots{position:absolute;left:562px;top:475px;display:flex;gap:5px}
.dots span{width:11px;height:11px;border-radius:50%;background:#c4c4cc;box-shadow:inset 0 1px 2px rgba(0,0,0,.5)}
.dots span.active{background:var(--white)}
.tagline{position:absolute;left:0;top:518px;width:1200px;text-align:center;color:var(--white);font-family:"Roboto Condensed",Arial,sans-serif;font-size:22px;line-height:28px}
.features{position:absolute;left:0;top:772px;width:1200px;height:348px}
.card{position:absolute;top:29px;width:272px;height:292px;background:var(--white);border:1px solid #dcd9db;text-align:center}
.card-about{left:131px}.card-community{left:463px}.card-signup{left:795px}
.card svg{position:absolute;left:96px;top:26px}
.card h2{position:absolute;left:0;top:122px;width:100%;font-family:"Roboto Condensed",Arial,sans-serif;font-weight:400;font-size:23px;color:var(--ink)}
.card p{position:absolute;left:8px;top:164px;width:256px;font-size:11.5px;line-height:18px;color:var(--muted)}
.card .btn{left:98px;top:238px;width:72px;height:32px;font-size:13px}
.site-footer{position:absolute;left:0;top:1120px;width:1200px;height:80px;background:var(--ink);color:var(--white)}
.legal{position:absolute;left:120px;top:37px;font-size:12px}
.legal span{margin:0 9px}
.social{position:absolute;left:940px;top:26px;display:flex;gap:5px}
.social span{width:31px;height:31px;border-radius:50%;background:var(--white)}
</style>
</head>
<body>
<div class="top-strip"></div>
<header class="site-header">
  <div class="brand">CORVANTA</div>
  <div class="btn btn-signup">SIGN UP</div>
  <div class="field field-user"></div>
  <div class="field field-pass"></div>
  <div class="btn btn-login">LOGIN</div>
  <div class="remember"><span class="box"></span>Remember me!</div>
  <div class="forgot">Forgot Password ?</div>
</header>

<section class="hero">
  <div class="slide-frame">
    <div class="slide-photo" role="img" aria-label="Photo of a smiling father carrying his son on his back under a bright blue sky">
      <div class="slide-people"></div>
      <div class="slide-brand">CORVANTA</div>
    </div>
  </div>
  <svg class="arrow arrow-prev" width="42" height="62" viewBox="0 0 42 62" aria-hidden="true">
    <path d="M42 0 A31 31 0 0 0 42 62 Z" fill="#f2f2f2"/>
    <path d="M36 17 L10 31 L36 45 Z" fill="#222"/>
  </svg>
  <svg class="arrow arrow-next" width="42" height="62" viewBox="0 0 42 62" aria-hidden="true">
    <path d="M0 0 A31 31 0 0 1 0 62 Z" fill="#f2f2f2"/>
    <path d="M6 17 L32 31 L6 45 Z" fill="#222"/>
  </svg>
  <div class="dots"><span></span><span class="active"></span><span></span><span></span><span></span></div>
  <p class="tagline">CORVANTA IS AN ONLINE&nbsp; COMMUNITY CENTRIC APPROACH TO WELLNESS THROUGH EDUCATION,<br>COMMUNICATION, AND BEHAVIORAL MANAGEMENT FOR PEOPLE WITH CHRONIC HEALTH CONDITIONS.</p>
</section>

<section class="features">
  <article class="card card-about">
    <svg width="80" height="80" viewBox="0 0 80 80" aria-hidden="true"><circle cx="40" cy="38" r="30" fill="var(--ink)"/></svg>
    <h2>ABOUT CORVANTA</h2>
    <p>perspiciatis unde omnis iste natus error sit voluptatem accusantium dolore ue laudantium, totam rem aperiam, eaque</p>
    <div class="btn">MORE</div>
  </article>
  <article class="card card-community">
    <svg width="80" height="80" viewBox="0 0 80 80" aria-hidden="true">
      <circle cx="40" cy="40" r="18" fill="none" stroke="var(--ink)" stroke-width="8"/>
      <circle cx="40" cy="8" r="7" fill="var(--ink)"/><circle cx="40" cy="72" r="7" fill="var(--ink)"/>
      <circle cx="8" cy="40" r="7" fill="var(--ink)"/><circle cx="72" cy="40" r="7" fill="var(--ink)"/>
    </svg>
    <h2>COMMUNITY HIGHLIGHTS</h2>
    <p>perspiciatis unde omnis iste natus error sit voluptatem accusantium dolore ue laudantium, totam rem aperiam, eaque</p>
    <div class="btn">MORE</div>
  </article>
  <article class="card card-signup">
    <svg width="80" height="80" viewBox="0 0 80 80" aria-hidden="true">
      <rect x="6" y="16" width="62" height="44" fill="none" stroke="var(--ink)" stroke-width="3"/>
      <rect x="10" y="20" width="20" height="24" fill="var(--ink)"/>
      <path d="M15 25 L15 38 L19 34 L23 40 L25 39 L21 33 L26 33 Z" fill="#fff"/>
      <path d="M36 26 H62 M36 34 H62 M36 42 H62 M12 50 H62" stroke="var(--ink)" stroke-width="3"/>
      <rect x="34" y="60" width="6" height="8" fill="var(--ink)"/>
      <path d="M20 74 Q37 64 54 74 Z" fill="var(--ink)"/>
    </svg>
    <h2>SIGN UP</h2>
    <p>perspiciatis unde omnis iste natus error sit voluptatem accusantium dolore ue laudantium, totam rem aperiam, eaque</p>
    <div class="btn">MORE</div>
  </article>
</section>

<footer class="site-footer">
  <div class="legal">© 2013 Corvanta All rights reserved.<span>|</span>Privacy<span>|</span>Terms of Use</div>
  <div class="social" aria-label="Social links"><span></span><span></span><span></span><span></span></div>
</footer>
</body>
</html>
```